Flyer for Dessert Cafe event launch

Hi
We are launching a new initiative at our cafe - this is the plan:
- We will open Saturday nights to serve desserts, tea and coffee and other after dinner deliciousness (no alcohol)
- Customers stop in and enjoy something sweets on the way home from dinner or movies. We'd decorate the garden with fairy lights, candles and lanterns and create a beautiful and relaxing (and romantic) after dinner atmosphere - maybe a little acoustic guitar
- For the menu we are thinking everything from chocolate mousse and cheesecake to tiramisu and dessert mocktails and even sorbet and gelato.
- The dessert cafe would probably trade from 7pm till 11pm.
Please check out www.brambelkitchen.com for our current branding feel.

We need an A4 flyer designed to promote this new venture.
I want the design to incorporate trees with fairy lights in them - and hearts - as we will be launching on Valentines Day evening (and the heart is part of our branding). Obviously the design needs to be tied in with our current branding - logo attached in various forms I am happy for you to use whichever fits best with your design. I have also attached some images that inspire me for this project - but they don't need to be used.

The following information will need to be included:

On the way home from dinner, or just craving something sweet?
Join us for Dessert!
Unwind - Relax - Indulge
7pm - 11pm every Saturday night
Starting on Valentines Day
All desserts handmade in-house - with love! *** Coffee *** Tea *** Mocktails *** Share platters available ***Gluten Free, Dairy Free and Vegan options *** Take-Away Available
Live Music

2248 Wattleridge Road, Kelvin Flats (five minutes from Coralport)
(03) 5391 8462
www.brambelkitchen.com
Please include the Facebook - Twiiter and Instagram Icons

```html
<!DOCTYPE html>
<html lang="en">
<head>
<meta charset="utf-8">
<title>Brambel Kitchen Café – Dessert Nights</title>
<link rel="stylesheet" href="https://fonts.googleapis.com/css2?family=Playball&family=Michroma&display=swap">
<style>
  :root {
    --ink-blue: #2b7fb4;
    --ink-blue-dark: #1f6596;
    --shadow-pink: #f2a3c4;
    --blossom-pink: #e9738a;
    --blossom-rose: #f3a9b4;
    --glow-amber: #f6c26a;
    --glow-cream: #fbe6c8;
    --paper: #ffffff;
    --logo-white: #ffffff;
  }
  html, body {
    margin: 0;
    padding: 0;
    width: 855px;
    height: 1200px;
    overflow: hidden;
    background: var(--paper);
  }
  .flyer {
    position: relative;
    width: 855px;
    height: 1200px;
    overflow: hidden;
    background: var(--paper);
    font-family: "Playball", cursive;
    color: var(--ink-blue);
  }
  .blossom-photo {
    position: absolute;
    left: 0; top: 0;
    width: 855px; height: 760px;
    background:
      radial-gradient(ellipse 260px 200px at 110px 120px, rgba(214,90,110,0.85), transparent 70%),
      radial-gradient(ellipse 300px 200px at 720px 110px, rgba(233,115,138,0.8), transparent 70%),
      radial-gradient(ellipse 280px 180px at 420px 420px, rgba(246,194,106,0.85), transparent 70%),
      radial-gradient(ellipse 220px 160px at 760px 380px, rgba(243,140,110,0.8), transparent 70%),
      radial-gradient(ellipse 200px 160px at 90px 460px, rgba(240,150,120,0.75), transparent 70%),
      linear-gradient(180deg, var(--blossom-rose) 0%, var(--glow-cream) 55%, rgba(255,255,255,0) 100%);
  }
  .dessert-photo {
    position: absolute;
    left: 0; top: 860px;
    width: 855px; height: 340px;
    background:
      radial-gradient(ellipse 130px 110px at 340px 200px, rgba(248,220,120,0.9), transparent 75%),
      radial-gradient(ellipse 70px 40px at 800px 150px, rgba(243,180,60,0.8), transparent 75%),
      radial-gradient(ellipse 80px 60px at 600px 140px, rgba(231,96,79,0.5), transparent 75%),
      linear-gradient(180deg, rgba(255,255,255,0) 0%, #f7f3ee 40%, #efe9e2 100%);
  }
  .brand-name {
    position: absolute;
    left: 0; top: 100px;
    width: 790px;
    text-align: center;
    font-size: 76px;
    line-height: 1;
    color: var(--logo-white);
    margin: 0;
    font-weight: 400;
  }
  .brand-name .brand-sub {
    display: block;
    font-size: 50px;
    margin-top: -4px;
    padding-left: 150px;
  }
  .line {
    position: absolute;
    left: 0;
    width: 855px;
    margin: 0;
    text-align: center;
    font-weight: 400;
    line-height: 1.1;
    white-space: nowrap;
    color: var(--ink-blue);
    text-shadow: 2px 2px 0 var(--shadow-pink);
  }
  .headline { font-size: 60px; }
  .call-to-action { font-size: 52px; }
  .call-to-action.motto { font-size: 60px; }
  .detail { font-size: 40px; }
  .offer { font-size: 44px; }
  .feature { font-size: 40px; }
  .contact {
    position: absolute;
    left: 0; top: 1022px;
    width: 845px;
    text-align: center;
    font-family: "Michroma", sans-serif;
    font-style: normal;
    color: var(--ink-blue-dark);
    text-transform: uppercase;
    font-size: 13px;
    line-height: 19px;
  }
  .contact p { margin: 0; }
  .contact .website { font-size: 16px; line-height: 26px; font-weight: 700; }
  .social { display: flex; justify-content: center; align-items: center; gap: 6px; font-size: 12px; line-height: 18px; }
  .social svg { display: block; }
</style>
</head>
<body>
<main class="flyer">
  <div class="blossom-photo" role="img" aria-label="Soft-focus photo of pink blossom trees glowing with warm fairy lights and hearts"></div>
  <div class="dessert-photo" role="img" aria-label="Photo of a plated white chocolate heart dessert with mango sauce and red petals"></div>

  <h1 class="brand-name">brambel kitchen<span class="brand-sub">café</span></h1>

  <p class="line headline" style="top:267px">On the way home from dinner,</p>
  <p class="line headline" style="top:325px">or just craving something</p>
  <p class="line headline" style="top:382px">sweet?</p>

  <p class="line call-to-action" style="top:481px">Join us for Dessert!</p>
  <p class="line call-to-action motto" style="top:537px">Unwind - Relax - Indulge</p>

  <p class="line detail" style="top:610px">7pm - 11pm every Saturday night</p>
  <p class="line detail" style="top:650px">Starting on Valentines Day</p>
  <p class="line detail" style="top:690px">All desserts handmade in-house</p>
  <p class="line detail" style="top:730px">with love!</p>

  <p class="line offer" style="top:776px">*** Coffee *** Tea *** Mocktails ***</p>
  <p class="line feature" style="top:826px">Share platters available</p>
  <p class="line feature" style="top:868px">Gluten Free, Dairy Free and Vegan options</p>
  <p class="line feature" style="top:913px">Take-Away Available</p>
  <p class="line feature" style="top:953px">*** Live Music ***</p>

  <address class="contact">
    <p>2248 Wattleridge Road, Kelvin Flats</p>
    <p>(five minutes from Coralport)</p>
    <p>(03) 5391 8462</p>
    <p class="website">www.brambelkitchen.com</p>
    <p class="social"><svg width="14" height="14" aria-hidden="true"><circle cx="7" cy="7" r="7" fill="var(--ink-blue)"/></svg>www.chatterpage.com/brambelkitchencafe</p>
    <p class="social"><svg width="14" height="14" aria-hidden="true"><circle cx="7" cy="7" r="7" fill="var(--ink-blue)"/></svg>tweetline.com/brambelkitchen</p>
    <p class="social"><svg width="14" height="14" aria-hidden="true"><circle cx="7" cy="7" r="7" fill="var(--ink-blue)"/></svg>brambelkitchen</p>
  </address>
</main>
</body>
</html>
```